Business card design needed

We are a gardening company who handle:
All Forms of gardens work including
Mowing
Pruning
edging
weeding
Poisoning
Landscaping
Minor Stump Removal
Rubbish Removal
and more

I want a card that look professional not cartoon style

Harlow Yards and Lawncare Service

Dean Marsholt
0486259041

```html
<!DOCTYPE html>
<html lang="en">
<head>
<meta charset="utf-8">
<title>Harlow Yards and Lawncare Service – Business Card</title>
<link href="https://fonts.googleapis.com/css2?family=Quicksand:wght@300;400;700&family=Open+Sans:wght@400;600&display=swap" rel="stylesheet">
<style>
  :root {
    --backdrop: #5b5b5d;
    --card-white: #ffffff;
    --card-grey: #e4e4e4;
    --band-black: #1b1b1b;
    --band-black-2: #262626;
    --accent-pink: #e0175f;
    --ink-dark: #141414;
    --ink-name: #6a6a6a;
    --ink-light: #f2f2f2;
    --icon-grey: #9a9a9a;
  }
  * { margin: 0; padding: 0; box-sizing: border-box; }
  html, body {
    width: 1200px; height: 871px; overflow: hidden;
    background: var(--backdrop);
  }
  .card {
    position: absolute; left: 100px; top: 150px;
    width: 1000px; height: 571px;
    background: linear-gradient(160deg, var(--card-white) 40%, var(--card-grey) 100%);
    box-shadow: 0 10px 30px rgba(0,0,0,0.35);
    overflow: hidden;
  }
  .company {
    position: absolute; right: 70px; top: 70px;
    text-align: right;
    font-family: "Quicksand", sans-serif; font-weight: 700;
    font-size: 46px; line-height: 1.15; letter-spacing: 1px;
  }
  .company__line1 { color: var(--accent-pink); }
  .company__line2 { color: var(--ink-dark); }
  .person {
    position: absolute; left: 60px; top: 230px;
    font-family: "Quicksand", sans-serif;
  }
  .person__name { font-size: 40px; font-weight: 300; color: var(--ink-name); }
  .person__name .surname { color: var(--accent-pink); }
  .person__role { font-size: 12px; color: var(--ink-name); letter-spacing: 1px; margin-top: -2px; }
  .contact-band {
    position: absolute; left: 0; top: 320px;
    width: 905px; height: 215px;
    background: linear-gradient(180deg, var(--band-black-2), var(--band-black));
  }
  .accent-bar {
    position: absolute; right: 30px; top: 320px;
    width: 50px; height: 251px;
    background: var(--accent-pink);
  }
  .contacts {
    position: absolute; left: 60px; top: 345px;
    list-style: none;
    font-family: "Open Sans", sans-serif; font-weight: 600;
    font-size: 20px; color: var(--ink-light); line-height: 1.3;
  }
  .contacts li { display: flex; align-items: flex-start; gap: 12px; margin-bottom: 6px; }
  .contacts .icon { flex: none; margin-top: 5px; }
  .contacts .web { color: var(--accent-pink); }
</style>
</head>
<body>
  <div class="card">
    <div class="company">
      <div class="company__line1">Harlow Yards</div>
      <div class="company__line2">Lawncare Service</div>
    </div>

    <div class="person">
      <div class="person__name">Dean <span class="surname">Marsholt</span></div>
      <div class="person__role">CEO</div>
    </div>

    <div class="contact-band"></div>
    <div class="accent-bar"></div>

    <ul class="contacts">
      <li>
        <svg class="icon" width="18" height="18" viewBox="0 0 18 18" aria-hidden="true">
          <rect x="1" y="1" width="16" height="16" rx="3" fill="none" stroke="var(--icon-grey)" stroke-width="1.5"/>
          <path d="M9 4a3.2 3.2 0 0 0-3.2 3.2C5.8 9.8 9 14 9 14s3.2-4.2 3.2-6.8A3.2 3.2 0 0 0 9 4z" fill="var(--icon-grey)"/>
        </svg>
        <span>14 Wattle Grove Road<br>Kelby Park 4127</span>
      </li>
      <li>
        <svg class="icon" width="18" height="18" viewBox="0 0 18 18" aria-hidden="true">
          <rect x="1" y="1" width="16" height="16" rx="3" fill="none" stroke="var(--icon-grey)" stroke-width="1.5"/>
          <path d="M6 4.5l2 2-1.2 1.3a6 6 0 0 0 3.4 3.4L11.5 10l2 2-1.3 1.5C9 13 5 9 4.5 5.8z" fill="var(--icon-grey)"/>
        </svg>
        <span>0486259041</span>
      </li>
      <li>
        <svg class="icon" width="18" height="18" viewBox="0 0 18 18" aria-hidden="true">
          <rect x="1" y="1" width="16" height="16" rx="3" fill="none" stroke="var(--icon-grey)" stroke-width="1.5"/>
          <rect x="4.5" y="5.5" width="9" height="7" fill="none" stroke="var(--icon-grey)" stroke-width="1.2"/>
          <path d="M4.5 5.5L9 9.5l4.5-4" fill="none" stroke="var(--icon-grey)" stroke-width="1.2"/>
        </svg>
        <span>info@harlowyards.com</span>
      </li>
      <li>
        <svg class="icon" width="18" height="18" viewBox="0 0 18 18" aria-hidden="true">
          <rect x="1" y="1" width="16" height="16" rx="3" fill="none" stroke="var(--icon-grey)" stroke-width="1.5"/>
          <circle cx="9" cy="9" r="4.5" fill="none" stroke="var(--icon-grey)" stroke-width="1.2"/>
          <path d="M4.5 9h9M9 4.5c-2 2.5-2 6.5 0 9M9 4.5c2 2.5 2 6.5 0 9" fill="none" stroke="var(--icon-grey)" stroke-width="1"/>
        </svg>
        <span class="web">harlowyards.com</span>
      </li>
    </ul>
  </div>
</body>
</html>
```